Bref créative
Business card design for
Keep-N-Cozy Self Storage, LLC
Simple
Dale Vinter
Manager
2870 Marlow Rd.
dvinter@mailquay.net
Bins-Ready-Now.net
The business card design should incorportate the logo from the logo project.

```html
<!DOCTYPE html>
<html lang="en">
<head>
<meta charset="utf-8">
<title>Keep-N-Cozy Self Storage Stationery</title>
<link href="https://fonts.googleapis.com/css2?family=Open+Sans:wght@400;600&display=swap" rel="stylesheet">
<style>
:root{
  --green:#1d5a33;
  --green-dark:#123d22;
  --gold:#b8a46c;
  --paper:#ffffff;
  --ink:#4a4a4a;
  --bg:#e9e6e1;
}
*{margin:0;padding:0;box-sizing:border-box}
html,body{width:1200px;height:341px;overflow:hidden;background:var(--bg);font-family:"Open Sans",sans-serif;color:var(--ink)}
.canvas{position:relative;width:1200px;height:341px}
.piece{position:absolute;background:var(--paper);box-shadow:0 2px 6px rgba(0,0,0,.25);overflow:hidden}
.piece svg.swoosh{position:absolute;left:0;bottom:0;width:100%}
.brand{display:flex;align-items:center;gap:4px;font-weight:600;color:var(--green);line-height:1.05;position:absolute}
.brand-mark{background:var(--green);flex:none}
.small{position:absolute;font-size:4px;line-height:1.4;color:var(--ink)}
.card-front{left:29px;top:132px;width:120px;height:62px}
.card-back{left:29px;top:210px;width:120px;height:66px}
.letterhead{top:19px;width:170px;height:300px}
.lh-1{left:228px}
.lh-2{left:410px}
.envelope{width:216px;height:106px}
.env-front-1{left:636px;top:84px}
.env-front-2{left:636px;top:204px}
.env-back-1{left:888px;top:74px;background:#f4f2ee}
.env-back-2{left:888px;top:204px;background:#f4f2ee}
</style>
</head>
<body>
<div class="canvas">

  <!-- Business card, front -->
  <div class="piece card-front">
    <div class="brand" style="left:5px;top:6px;font-size:7px"><span class="brand-mark" style="width:8px;height:8px"></span>Keep-N-Cozy<br>Storage</div>
    <div class="small" style="right:6px;top:8px;text-align:right;font-size:4.5px"><b style="color:var(--green)">Dale Vinter</b><br>Manager</div>
    <div class="small" style="right:6px;top:22px;text-align:right">2870 Marlow Rd.<br>Tel 555-201-4476<br>dvinter@mailquay.net<br>Bins-Ready-Now.net</div>
    <svg class="swoosh" viewBox="0 0 120 14" preserveAspectRatio="none" height="14"><path d="M0 14V4C40 12 80 12 120 2V14Z" fill="var(--green)"/></svg>
  </div>

  <!-- Business card, back -->
  <div class="piece card-back">
    <div class="brand" style="left:5px;top:6px;font-size:7px"><span class="brand-mark" style="width:8px;height:8px"></span>Keep-N-Cozy<br>Storage</div>
    <div class="small" style="left:6px;top:30px"><b style="color:var(--green)">Dale Vinter</b><br>Manager<br>dvinter@mailquay.net</div>
    <svg class="swoosh" viewBox="0 0 120 12" preserveAspectRatio="none" height="12"><path d="M0 12V5C40 11 80 11 120 3V12Z" fill="var(--green)"/></svg>
  </div>

  <!-- Letterhead 1 -->
  <div class="piece letterhead lh-1">
    <div class="brand" style="left:52px;top:8px;font-size:9px"><span class="brand-mark" style="width:11px;height:11px"></span>Keep-N-Cozy<br>Storage</div>
    <div class="small" style="left:112px;top:10px">2870 Marlow Rd.<br>Tel 555-201-4476<br>Bins-Ready-Now.net</div>
    <svg class="swoosh" viewBox="0 0 170 22" preserveAspectRatio="none" height="22"><path d="M0 22V6C50 18 110 18 170 10V22Z" fill="var(--green)"/></svg>
  </div>

  <!-- Letterhead 2 -->
  <div class="piece letterhead lh-2">
    <svg viewBox="0 0 170 14" preserveAspectRatio="none" width="170" height="14" style="position:absolute;top:0;left:0"><path d="M0 0H170V4C110 12 50 12 0 6Z" fill="var(--green)"/></svg>
    <div class="brand" style="left:8px;top:16px;font-size:9px"><span class="brand-mark" style="width:11px;height:11px"></span>Keep-N-Cozy<br>Storage</div>
    <svg class="swoosh" viewBox="0 0 170 14" preserveAspectRatio="none" height="14"><path d="M0 14V8C60 2 120 2 170 8V14Z" fill="var(--green)"/></svg>
    <div class="small" style="left:0;right:0;bottom:2px;text-align:center;color:#fff">2870 Marlow Rd. · Bins-Ready-Now.net</div>
  </div>

  <!-- Envelope front 1 -->
  <div class="piece envelope env-front-1">
    <div class="brand" style="left:8px;top:8px;font-size:7px"><span class="brand-mark" style="width:9px;height:9px"></span>Keep-N-Cozy<br>Storage</div>
    <div class="small" style="left:8px;top:28px">2870 Marlow Rd.</div>
    <svg class="swoosh" viewBox="0 0 216 14" preserveAspectRatio="none" height="14"><path d="M0 14V4C70 14 150 12 216 2V14Z" fill="var(--green)"/></svg>
  </div>

  <!-- Envelope front 2 -->
  <div class="piece envelope env-front-2">
    <svg viewBox="0 0 216 12" preserveAspectRatio="none" width="216" height="12" style="position:absolute;top:0;left:0"><path d="M0 0H216V4C150 12 70 12 0 4Z" fill="var(--green)"/></svg>
    <div class="brand" style="left:8px;top:16px;font-size:7px"><span class="brand-mark" style="width:9px;height:9px"></span>Keep-N-Cozy<br>Storage</div>
    <svg class="swoosh" viewBox="0 0 216 12" preserveAspectRatio="none" height="12"><path d="M0 12V6C70 0 150 0 216 6V12Z" fill="var(--green)"/></svg>
  </div>

  <!-- Envelope back, gold flap -->
  <div class="piece envelope env-back-1">
    <svg viewBox="0 0 216 106" width="216" height="106" style="position:absolute;inset:0">
      <path d="M0 106L108 50L216 106" fill="none" stroke="#d8d4cc" stroke-width="1"/>
      <path d="M0 0H216V10L108 52L0 10Z" fill="var(--gold)"/>
      <path d="M0 0H216V4L108 44L0 4Z" fill="var(--green)"/>
    </svg>
    <div class="brand" style="left:92px;top:16px;font-size:5px;color:#fff"><span class="brand-mark" style="width:6px;height:6px;background:#fff"></span>Keep-N-Cozy<br>Storage</div>
  </div>

  <!-- Envelope back, green flap -->
  <div class="piece envelope env-back-2">
    <svg viewBox="0 0 216 106" width="216" height="106" style="position:absolute;inset:0">
      <path d="M0 106L108 50L216 106" fill="none" stroke="#d8d4cc" stroke-width="1"/>
      <path d="M0 0H216V8L108 48L0 8Z" fill="var(--green)"/>
    </svg>
  </div>

</div>
</body>
</html>
```